New business card for our new logo

I have a brand new, existing logo. Now I need it on a new business card. The new card should include the following:

English language training
Translations
Interpreting Services (remote and in-person)

Target Market(s)

We are targeting international companies with foreign investment in the United States as well as domestic companies, medical offices, law offices, and non-profits that have non-native English speakers as their clients.

Contact Information for Business Card

Delia Brancombe, President
418 Garrow St.
Indianapolis, IN 46203
(317) 548-3162
info@tallpinewordworks.com
www.tallpinewordworks.com

Font styles to use
Sans Serif

Colors
0392cd
3176b5
abd036
9bcb3b
f04a50
f78f20

Requirements
Must have
• It must include our logo and business card details
Nice to have
• I would like to see a layout that is uncluttered and conveys trust and dependability, as well as the feelings of being friendly and approachable.

It would be nice to have icons for English language training, translating, and interpreting.
Should not have
• No pink, yellow, or purple

```html
<!DOCTYPE html>
<html lang="en">
<head>
<meta charset="utf-8">
<title>Tall Pine Wordworks – Business Card</title>
<link href="https://fonts.googleapis.com/css2?family=Montserrat:wght@500;600;700&family=Open+Sans:wght@400;600&display=swap" rel="stylesheet">
<style>
  :root{
    --brand-blue:#2874b7;
    --paper:#ffffff;
    --ink:#3a3a3a;
    --backdrop:#1e1e1e;
    --rule:#2874b7;
  }
  *{box-sizing:border-box;margin:0;padding:0}
  html,body{width:1200px;height:988px;overflow:hidden;background:var(--backdrop)}
  .sheet{position:relative;width:1200px;height:988px}
  .card{position:absolute;width:700px;height:400px;border-radius:22px;left:250px;overflow:hidden}
  .card--front{top:48px;background:var(--brand-blue)}
  .card--back{top:540px;background:var(--paper)}

  .brand{display:flex;align-items:center;gap:22px;position:absolute}
  .brand__dot{border-radius:50%;flex:none}
  .brand__name{font-family:"Montserrat",sans-serif;font-weight:600;line-height:.98;letter-spacing:.5px}
  .card--front .brand{left:160px;top:105px}
  .card--front .brand__dot{width:180px;height:180px;background:var(--paper)}
  .card--front .brand__name{color:var(--paper);font-size:50px}
  .card--back .brand{left:44px;top:48px;gap:18px}
  .card--back .brand__dot{width:118px;height:118px;background:var(--brand-blue)}
  .card--back .brand__name{color:var(--brand-blue);font-size:33px}

  .rule{position:absolute;inset:0;pointer-events:none}

  .person{position:absolute;right:52px;top:42px;text-align:right}
  .person__name{font-family:"Montserrat",sans-serif;font-weight:700;font-size:26px;color:var(--brand-blue);letter-spacing:.5px}
  .person__role{font-family:"Open Sans",sans-serif;font-size:15px;color:var(--ink);margin-top:2px}

  .services{position:absolute;right:40px;top:128px;list-style:none;text-align:right}
  .services li{display:flex;align-items:center;justify-content:flex-end;gap:10px;height:38px;font-family:"Open Sans",sans-serif;font-size:16px;color:var(--ink)}
  .services svg{width:28px;height:28px;flex:none}

  .contact{position:absolute;left:62px;top:262px;list-style:none;font-family:"Open Sans",sans-serif;font-size:15px;color:var(--ink)}
  .contact li{display:flex;align-items:flex-start;gap:12px;line-height:22px}
  .contact svg{width:14px;height:14px;flex:none;margin-top:4px}
  .contact .web-domain{color:var(--brand-blue)}
</style>
</head>
<body>
<main class="sheet">
  <section class="card card--front" aria-label="Card front">
    <div class="brand">
      <span class="brand__dot"></span>
      <p class="brand__name">Tall Pine<br>Word<br>works</p>
    </div>
  </section>

  <section class="card card--back" aria-label="Card back">
    <div class="brand">
      <span class="brand__dot"></span>
      <p class="brand__name">Tall Pine<br>Word<br>works</p>
    </div>

    <svg class="rule" viewBox="0 0 700 400" aria-hidden="true">
      <line x1="648" y1="108" x2="62" y2="240" stroke="var(--rule)" stroke-width="1.3"/>
    </svg>

    <div class="person">
      <p class="person__name">DELIA BRANCOMBE</p>
      <p class="person__role">President</p>
    </div>

    <ul class="services">
      <li>Translations
        <svg viewBox="0 0 28 28" fill="none" stroke="var(--brand-blue)" stroke-width="1.4"><circle cx="14" cy="14" r="13"/><rect x="6" y="8" width="8" height="6" rx="1.5"/><rect x="14" y="13" width="8" height="6" rx="1.5"/></svg>
      </li>
      <li>English language training
        <svg viewBox="0 0 28 28" fill="none" stroke="var(--brand-blue)" stroke-width="1.4"><circle cx="14" cy="14" r="13"/><rect x="7" y="8" width="14" height="10" rx="1"/><line x1="10" y1="12" x2="18" y2="12"/><line x1="10" y1="15" x2="15" y2="15"/></svg>
      </li>
      <li>Interpreting Services
        <svg viewBox="0 0 28 28" fill="none" stroke="var(--brand-blue)" stroke-width="1.4"><circle cx="14" cy="14" r="13"/><circle cx="10" cy="10" r="2"/><circle cx="18" cy="10" r="2"/><path d="M6.5 20v-3.5a3.5 3.5 0 0 1 7 0V20M14.5 20v-3.5a3.5 3.5 0 0 1 7 0V20"/></svg>
      </li>
    </ul>

    <ul class="contact">
      <li>
        <svg viewBox="0 0 14 14"><path d="M7 0a5 5 0 0 0-5 5c0 3.6 5 9 5 9s5-5.4 5-9a5 5 0 0 0-5-5zm0 7a2 2 0 1 1 0-4 2 2 0 0 1 0 4z" fill="var(--brand-blue)"/></svg>
        <span>418 Garrow St.<br>Indianapolis, IN 46203</span>
      </li>
      <li>
        <svg viewBox="0 0 14 14"><path d="M3 1l2 3-1.3 1.5a8 8 0 0 0 4.8 4.8L10 9l3 2-1 2.5C6 13.5.5 8 .5 2z" fill="var(--brand-blue)"/></svg>
        <span>(317) 548-3162</span>
      </li>
      <li>
        <svg viewBox="0 0 14 14"><rect x="0.5" y="2.5" width="13" height="9" fill="var(--brand-blue)"/><path d="M1 3l6 5 6-5" stroke="#fff" fill="none" stroke-width="1.1"/></svg>
        <span>info@tallpinewordworks.com</span>
      </li>
      <li>
        <svg viewBox="0 0 14 14"><circle cx="7" cy="7" r="6.5" fill="var(--brand-blue)"/><path d="M.5 7h13M7 .5c-3 3.5-3 9.5 0 13M7 .5c3 3.5 3 9.5 0 13" stroke="#fff" stroke-width=".9" fill="none"/></svg>
        <span>www.<span class="web-domain">tallpinewordworks</span>.com</span>
      </li>
    </ul>
  </section>
</main>
</body>
</html>
```